EDDM (Every Door Direct Mail) Mailer - Direct Mail Piece

We want to create a EDDM Mailer (Every Door Direct Mail)
We are looking to create a new mailer to be sent to prospective new customers. We pinpoint these mailings to specific customers in the communities we are looking to grow our business. These are High End Communities. High Wealth Clients.

We have included some examples of other supporting items we have used in the past. PLEASE NOTE: We are NOT looking to promote the R & K Pool Plastering. That was a one time promotion. We are looking to focus on our company Tidewell and the services we offer. The current EDDM Mailer is 6 1/4 X 9 and that sample was attached.

Our goal is to get the customers to call us

561 TIDEWELL = 561-203-8419
844 TIDEWELL = 844-203-8419 (Toll Free)
www.tidewell-example.com
www.facebook.com/TidewellSvc

We Are Professional - Provide Fast Reliable Service and Repairs

We Offer:
Pool Service
Pool Repairs
Pool Equipment Repairs
Pool Remodeling
Pool Resurfacing
Pool Tile Installation or Repair
Pool Deck Installations
Pool Equipment Installation or Repair
Pool Leak Detection and Leak Repairs
Licensed and Insured

We send an e-mail after we service the pool showing what employee was there on what day and time and what was done. (GPS Date & Time Stamped) This includes Pictures of YOUR Pool! Our Customers Love This Feature! They know who was there, when they were there and what they did! This e-mail is sent before our Pool Technician leaves the customers home all in real time.

All Employees are tracked by GPS so we know were they are and how much time they spend at each clients home. All employees where company uniforms and drive company vehicles with proper logos, phone numbers and website address.

Please Ask any Questions. We want to make sure we are sending a clear message.

Thank You For Your Help!

Target Market(s)

High End Communities. High Wealth Clients.

Requirements
Must have
• Call To Action.
We Want Them To Pick Up The Phone and CALL US!

New Customers Get One Month FREE
Nice to have
• Professional Look and Feel - Clean and Professional

```html
<!DOCTYPE html>
<html lang="en">
<head>
<meta charset="utf-8">
<title>Tidewell EDDM Mailer</title>
<link rel="stylesheet" href="https://fonts.googleapis.com/css2?family=Lato:wght@400;700&family=Oswald:wght@500;600&display=swap">
<style>
:root{
  --stage:#d9d9d9;
  --shadow:#9a9a9a;
  --teal:#1a8bb0;
  --teal-dark:#1f5466;
  --orange:#f8b133;
  --orange-deep:#f4a51c;
  --white:#ffffff;
  --paper:#f2f2f2;
  --ink:#333333;
  --red:#e8141b;
  --yellow:#ffd23a;
  --social:#3b5998;
}
*{margin:0;padding:0;box-sizing:border-box}
html,body{width:1200px;height:1200px;overflow:hidden;background:var(--stage)}
body{position:relative;font-family:'Lato',sans-serif}
.card-shadow{position:absolute;width:653px;height:477px;background:var(--shadow)}
.card{position:absolute;left:279px;width:653px;height:477px;overflow:hidden}

/* front */
.front{top:68px;background:linear-gradient(to bottom,var(--orange) 0 53%,var(--teal) 53% 100%)}
.front-frame{position:absolute;left:18px;top:18px;width:618px;height:441px;background:var(--white)}
.front-photo{position:absolute;left:23px;top:24px;width:608px;height:428px;
  background:linear-gradient(to bottom,#7fa35a 0%,#c9a98a 30%,#e5b79a 50%,#2fb7e6 68%,#6fd4f5 100%)}
.logo-tab{position:absolute;left:197px;top:24px;width:218px;height:88px;background:var(--white);border-radius:0 0 40px 40px}
.logo{position:absolute;left:0;right:0;top:24px;text-align:center}
.logo-mark{display:inline-block;width:16px;height:16px;border-radius:50%;background:var(--orange);vertical-align:middle;margin-right:6px}
.logo-name{font-family:'Oswald',sans-serif;font-weight:600;font-size:26px;color:var(--teal-dark);vertical-align:middle;letter-spacing:1px}
.logo-tag{font-family:'Oswald',sans-serif;font-weight:500;font-size:8.5px;color:var(--teal-dark);margin-top:2px}
.starburst{position:absolute;left:46px;top:258px;width:136px;height:136px}
.starburst-text{position:absolute;left:46px;top:296px;width:136px;text-align:center;font-family:'Oswald',sans-serif;color:var(--yellow);line-height:1.15}
.starburst-text .small{font-size:10px;font-weight:500}
.starburst-text .big{font-size:32px;font-weight:600;color:#ffb52a;line-height:1}
.banner{position:absolute;font-family:'Oswald',sans-serif;font-weight:600;color:var(--white);white-space:nowrap;text-align:center}
.banner-weekly{left:169px;top:359px;width:315px;height:28px;background:var(--teal-dark);font-size:20px;line-height:28px}
.banner-cleaning{left:116px;top:392px;width:422px;height:27px;background:var(--orange-deep);font-size:20px;line-height:27px}
.front-url{position:absolute;left:0;right:0;top:424px;text-align:center;font-size:13px;font-weight:700;letter-spacing:3px;color:var(--ink)}

/* back */
.back{top:630px;background:var(--white)}
.back svg.shapes{position:absolute;left:0;top:0}
.tag{position:absolute;color:var(--white);font-size:15px;font-weight:700;line-height:25px;padding-left:25px}
.tick-list{position:absolute;list-style:none}
.tick-list li{position:relative;padding-left:17px;white-space:nowrap}
.tick-list li::before{content:"";position:absolute;left:0;top:50%;width:8px;height:8px;margin-top:-5px;border:1px solid currentColor;border-radius:50%}
.list-are{left:26px;top:52px;color:var(--white);font-size:14px}
.list-are li{height:22.5px;line-height:22.5px}
.list-offer{left:26px;top:208px;color:var(--teal-dark);font-size:14px}
.list-offer li{height:20.6px;line-height:20.6px}
.feature-copy{position:absolute;left:298px;top:57px;width:322px;font-size:8px;line-height:10.6px;color:var(--ink);text-align:justify}
.feature-copy p+p{margin-top:10px}
.phones{position:absolute;right:32px;top:180px;text-align:right;color:var(--white);font-size:16px;line-height:26px}
.back-footer{position:absolute;left:25px;top:429px;display:flex;align-items:center;gap:12px;color:var(--white);white-space:nowrap}
.back-url{font-size:12px;font-weight:700;letter-spacing:1.2px}
.social{font-size:13px;display:flex;align-items:center}
.social-mark{display:inline-block;width:12px;height:12px;background:var(--social);margin-right:5px}
.indicia{position:absolute;left:569px;top:322px;width:50px;height:49px;border-left:1px solid #bbb;border-top:1px solid #bbb;font-family:Arial,sans-serif;font-size:6px;line-height:8px;text-align:center;padding-top:6px;color:#222}
.indicia b{display:block}
.address-box{position:absolute;left:422px;top:378px;width:198px;height:62px;border:1px solid #888;padding:16px 20px;font-family:Arial,sans-serif;font-size:10.5px;line-height:13.5px;color:#222}
</style>
</head>
<body>

<div class="card-shadow" style="left:267px;top:81px"></div>
<section class="card front">
  <div class="front-frame"></div>
  <div class="front-photo" role="img" aria-label="Smiling family in sunglasses together in a bright blue swimming pool"></div>
  <div class="logo-tab">
    <div class="logo">
      <span class="logo-mark"></span><span class="logo-name">TIDEWELL</span>
      <div class="logo-tag">TRUSTED PROFESSIONAL POOL SERVICE</div>
    </div>
  </div>
  <svg class="starburst" viewBox="0 0 100 100" aria-hidden="true">
    <polygon fill="#e8141b" points="50,0 55,10 63,2 65,13 75,7 74,18 85,15 81,26 93,26 86,35 97,38 88,45 99,50 88,55 97,62 86,65 93,74 81,74 85,85 74,82 75,93 65,87 63,98 55,90 50,100 45,90 37,98 35,87 25,93 26,82 15,85 19,74 7,74 14,65 3,62 12,55 1,50 12,45 3,38 14,35 7,26 19,26 15,15 26,18 25,7 35,13 37,2 45,10"/>
    <circle cx="50" cy="50" r="36" fill="#ee1c22"/>
  </svg>
  <div class="starburst-text">
    <div class="small">NEW CUSTOMERS</div>
    <div class="small">GET ONE MONTH</div>
    <div class="big">FREE</div>
  </div>
  <div class="banner banner-weekly">POOL SERVICES INCLUDE WEEKLY</div>
  <div class="banner banner-cleaning">SWIMMING POOL CLEANING &amp; MAINTENANCE</div>
  <div class="front-url">www.tidewell-example.com</div>
</section>

<div class="card-shadow" style="left:267px;top:643px"></div>
<section class="card back">
  <svg class="shapes" width="653" height="477" viewBox="0 0 653 477" aria-hidden="true">
    <rect x="273" y="0" width="380" height="174" fill="var(--paper)"/>
    <polygon points="0,0 273,0 227,158 0,158" fill="var(--teal)"/>
    <polygon points="273,0 283,0 242,112 232,112" fill="var(--orange)"/>
    <polygon points="227,158 255,158 230,147" fill="#b07a1e"/>
    <polygon points="0,158 255,158 342,406 0,406" fill="var(--orange)"/>
    <polygon points="261,174 653,174 653,236 281,236" fill="var(--teal)"/>
    <polygon points="292,265 300,265 352,406 342,406" fill="var(--teal)"/>
    <polygon points="0,406 352,406 324,477 0,477" fill="var(--teal)"/>
    <polygon points="0,18 112,18 100,43 0,43" fill="var(--orange)"/>
    <polygon points="284,18 460,18 448,43 272,43" fill="var(--teal)"/>
    <polygon points="0,175 124,175 112,200 0,200" fill="var(--teal)"/>
  </svg>
  <div class="tag" style="left:0;top:18px">WE ARE:</div>
  <ul class="tick-list list-are">
    <li>Professional</li><li>Reliable</li><li>Responsive</li><li>Fast Service and Repairs</li>
  </ul>
  <div class="tag" style="left:263px;top:18px">BIGGEST FEATURE:</div>
  <div class="feature-copy">
    <p>We send an e-mail after we service the pool showing what employee was there on what day and time and what was done. (Time &amp; Date Stamp) This includes Pictures Of The Pools! The Customers Love This Feature! They know WHO was there, WHEN they were there and WHAT they Did! This e-mail is sent before our Pool Technician leaves the customers home all in real time.</p>
    <p>All Employees are tracked by GPS so we know were they are and how much time they spend at each clients home. All employees where company uniforms and drive company vehicles with proper logos, phone numbers and website address.</p>
  </div>
  <div class="phones">
    <div>561 TIDEWELL = 561-203-8419</div>
    <div>844 TIDEWELL = 844-203-8419 (TOLL FREE)</div>
  </div>
  <div class="tag" style="left:0;top:175px">WE OFFER:</div>
  <ul class="tick-list list-offer">
    <li>Pool Service</li><li>Pool Repairs</li><li>Pool Equipment Repairs</li><li>Pool Remodeling</li><li>Pool Resurfacing</li><li>Pool Tile Installation or Repair</li><li>Pool Deck Installations</li><li>Pool Equipment Installation or Repair</li><li>Licensed and Insured</li>
  </ul>
  <div class="back-footer">
    <span class="back-url">www.tidewell-example.com</span>
    <span class="social"><span class="social-mark"></span>/TidewellSvc</span>
  </div>
  <div class="indicia">PRSRT STD<br>ECRWSS<br>U.S. POSTAGE<b>PAID</b>EDDM RETAIL</div>
  <div class="address-box">Local<br>Postal Customer</div>
</section>

</body>
</html>
```